I am a Financial Adviser specialising in Aged Care Advice. We provide financial advice and assistance to families with loved ones entering an Aged Care facility.
We need a flyer detailing the Aged Care Packages that we offer. There will be 3 main packages & then other add ons. I need an area where the client can sign off on the package/s that they choose. I have attached a sample to demonstrate the required layout, and a copy of content. I would like the flyer to have an image as per the attached sample, and to be designed in soft pastels, blues, greens.

Financial

```html
<!DOCTYPE html>
<html lang="en">
<head>
<meta charset="utf-8">
<title>Aged Care Services – Harbourline Advisory</title>
<link href="https://fonts.googleapis.com/css2?family=Lilita+One&family=Oswald:wght@500&family=Source+Sans+3:ital,wght@0,400;0,600;1,400&display=swap" rel="stylesheet">
<style>
  :root {
    --sky: #3fb4e6;
    --leaf: #9cc92c;
    --gold: #d8b02a;
    --rose: #e462a6;
    --navy: #1f5e8e;
    --ink: #222;
    --paper: #fff;
    --meadow-top: #e8f3c4;
    --meadow-bottom: #cfe685;
  }
  * { box-sizing: border-box; margin: 0; padding: 0; }
  html, body { width: 881px; height: 1200px; overflow: hidden; }
  body {
    position: relative;
    font-family: "Source Sans 3", sans-serif;
    color: var(--ink);
    background: linear-gradient(180deg, var(--meadow-top) 0%, var(--meadow-bottom) 100%);
  }
  .hero-photo {
    position: absolute; left: 0; top: 0; width: 881px; height: 600px;
    background: linear-gradient(180deg, #a9c48a 0%, #7fa356 35%, #8fbb4e 65%, #c9e38e 88%, rgba(216,236,160,0) 100%);
  }
  .masthead {
    position: absolute; left: 0; top: 25px; width: 881px; height: 112px;
    background: rgba(255,255,255,0.82);
    border-top: 2px solid var(--gold);
    border-bottom: 2px solid var(--gold);
  }
  .brand {
    position: absolute; left: 22px; top: 44px;
    display: flex; align-items: center; gap: 7px;
    font-size: 16px; font-weight: 600; color: #222; white-space: nowrap;
  }
  .brand-dot { width: 12px; height: 12px; border-radius: 50%; background: var(--gold); flex: none; }
  .masthead-title {
    position: absolute; left: 230px; top: 22px; width: 632px;
    display: flex; justify-content: space-between;
    font-family: "Lilita One", sans-serif; font-size: 60px; line-height: 1;
    font-weight: 400; white-space: nowrap;
    text-shadow: 2px 3px 3px rgba(0,0,0,0.25);
  }
  .masthead-title .blue { color: var(--sky); }
  .masthead-title .green { color: var(--leaf); }

  .package { position: absolute; left: 0; width: 881px; }
  .tick-box {
    position: absolute; left: 38px; width: 32px; height: 32px;
    background: var(--paper); border: 3px solid var(--gold);
  }
  .package-name {
    position: absolute; left: 86px;
    font-family: "Lilita One", sans-serif; font-size: 27px; line-height: 1; font-weight: 400;
    color: var(--sky); letter-spacing: 1px; white-space: nowrap;
    text-shadow: 1px 2px 2px rgba(0,0,0,0.2);
  }
  .tagline {
    position: absolute; right: 60px; width: 330px; text-align: center;
    font-family: "Oswald", sans-serif; font-style: italic; font-weight: 500;
    font-size: 18px; color: var(--rose); white-space: nowrap;
  }
  .details {
    position: absolute; left: 70px; width: 776px;
    background: var(--paper); border: 3px solid var(--gold);
  }
  .benefit {
    position: absolute; left: 494px; width: 336px; height: 57px;
    background: var(--paper); border: 3px solid var(--gold);
    font-family: "Lilita One", sans-serif; font-size: 44px; line-height: 51px;
    text-align: center; color: var(--leaf); letter-spacing: 1px;
    text-shadow: 1px 2px 2px rgba(0,0,0,0.25);
  }
  .includes {
    position: absolute; font-size: 20.5px; color: var(--navy); font-weight: 400; white-space: nowrap;
  }
  .points { position: absolute; list-style: none; font-size: 17.5px; line-height: 21.5px; white-space: nowrap; }
  .points li::before { content: "•"; margin-right: 6px; }
  .disclaimer {
    position: absolute; left: 108px; top: 714px;
    font-size: 15.5px; font-style: italic; white-space: nowrap;
  }
</style>
</head>
<body>
  <div class="hero-photo" role="img" aria-label="Smiling three-generation family of grandparents, parents and two children sitting together on grass in a sunny park"></div>

  <header class="masthead">
    <div class="brand"><span class="brand-dot"></span>Harbourline Advisory</div>
    <h1 class="masthead-title"><span class="blue">AGED</span><span class="blue">CARE</span><span class="green">SERVICES</span></h1>
  </header>

  <section class="package">
    <div class="tick-box" style="top:578px"></div>
    <h2 class="package-name" style="top:581px">ESSENTIALS PACKAGE $770</h2>
    <p class="tagline" style="top:562px">...When you know what you want...</p>
    <div class="details" style="top:622px;height:121px"></div>
    <div class="benefit" style="top:592px">PEACE OF MIND</div>
    <ul class="points" style="left:108px;top:636px">
      <li>Explanation of Aged Care Fees and Charges</li>
      <li>Preliminary Home/Assets Assessment*</li>
      <li>Estimated Means Tested Fee Calculation*</li>
    </ul>
    <ul class="points" style="left:505px;top:657px">
      <li>Preliminary Aged Care Costs*</li>
      <li>Estimated Cash Flow Scenario*</li>
    </ul>
    <p class="disclaimer">*Please note this is general factual information only.&nbsp; We do not provide any specific personal information.</p>
  </section>

  <section class="package">
    <div class="tick-box" style="top:794px"></div>
    <h2 class="package-name" style="top:797px">ADVANTAGE PACKAGE $2,970</h2>
    <p class="tagline" style="top:778px">...When you need to know all the options...</p>
    <div class="details" style="top:836px;height:121px"></div>
    <div class="benefit" style="top:810px">CONFIDENCE</div>
    <p class="includes" style="left:110px;top:849px">ESSENTIALS Package plus</p>
    <ul class="points" style="left:108px;top:881px">
      <li>Analyse and Strategize Aged Care costs</li>
      <li>Compare up to 5 Strategy options</li>
      <li>Minimise Aged Care Costs (where possible)</li>
    </ul>
    <ul class="points" style="left:473px;top:881px">
      <li>Maximise Age Pension Income (where possible)</li>
      <li>Prepare a Full Statement of Advice (SOA)</li>
      <li>Implementation of Aged Care Strategy</li>
    </ul>
  </section>

  <section class="package">
    <div class="tick-box" style="top:1003px"></div>
    <h2 class="package-name" style="top:1006px">PLATINUM PACKAGE $5,940</h2>
    <p class="tagline" style="top:990px">...When you need someone to take charge...</p>
    <div class="details" style="top:1048px;height:117px"></div>
    <div class="benefit" style="top:1020px">CONVENIENCE</div>
    <p class="includes" style="left:110px;top:1061px">ADVANTAGE Package plus</p>
    <ul class="points" style="left:108px;top:1091px">
      <li>Liase with the Aged Care Facility</li>
      <li>Pension/Veterans Agency Nominee</li>
      <li>Post Entry Review</li>
    </ul>
    <ul class="points" style="left:505px;top:1091px">
      <li>Post Implementation SOA (if required)</li>
      <li>Annual Review</li>
    </ul>
  </section>
</body>
</html>
```